Business card design for counselling and psychotherapy practice

I am seeking a business card for a new venture into private practice. I am based in Brisbane Qld Australia. I provide holistic counselling and psychotherapy to individuals and groups.
Some words that describe the underpinnings of this practice would include: being, becoming, awareness, wholeness, contact, safety, acceptance, relationship, gestalt, paradox, interconnected, nature, process.
I would like to see designs that include earth colours.
The overall design should communicate safety and a curiosity of being and becoming.
Target Market(s)
this design is marketed toward women, professionals, lesbian, transgender, mothers
Industry/Entity Type
Safety
Contact Information for Business Card
Still Harbour
Counselling and Psychotherapy
Wren Callow
ph: 0412739506
email: wren.stillharbour@examplemail.test
www.stillharbourcounselling&psychotherapy.test
Logo styles of interest
Abstract Logo
Look and feel

```html
<!DOCTYPE html>
<html lang="en">
<head>
<meta charset="utf-8">
<title>Still Harbour Counselling and Psychotherapy – Business Cards</title>
<link href="https://fonts.googleapis.com/css2?family=Playfair+Display:wght@800;900&family=Questrial&family=Lato:wght@400&display=swap" rel="stylesheet">
<style>
  :root {
    --page-bg: #eee9e1;
    --teal: #1f8f92;
    --teal-deep: #19787e;
    --sand: #e6d5b8;
    --clay: #b57a4b;
    --bark: #7a5a3c;
    --band-earth: #a88a66;
    --white: #ffffff;
    --ink: #2b241d;
    --title-shadow: rgba(40, 25, 10, 0.55);
  }
  * { margin: 0; padding: 0; box-sizing: border-box; }
  html, body { width: 1200px; height: 960px; overflow: hidden; background: var(--page-bg); }
  .sheet {
    position: relative; width: 1200px; height: 960px;
    display: flex; flex-direction: column; align-items: center; justify-content: center; gap: 40px;
  }
  .card {
    position: relative; width: 760px; height: 434px; overflow: hidden;
    box-shadow: 0 10px 28px rgba(60, 40, 20, 0.22);
  }
  .card svg.decor { position: absolute; inset: 0; width: 100%; height: 100%; }

  /* Front card: waves and diagonal lines */
  .card--waves { background: var(--teal); }
  .card--waves .title {
    position: absolute; left: 52px; top: 62px; width: 680px;
    font-family: "Playfair Display", serif; font-weight: 900;
    font-size: 40px; line-height: 1.12; color: var(--white);
  }
  .card--waves .contact {
    position: absolute; left: 0; top: 286px; list-style: none;
    font-family: "Lato", sans-serif; font-size: 19px; color: var(--white);
  }
  .card--waves .contact li { display: flex; align-items: center; height: 34px; }
  .card--waves .contact li::before {
    content: ""; display: block; width: 28px; height: 2px; background: var(--sand); margin-right: 40px;
  }

  /* Back card: boxed rows and bottom band */
  .card--band { background: var(--teal-deep); }
  .card--band .title {
    position: absolute; left: 70px; top: 34px; width: 680px;
    font-family: "Playfair Display", serif; font-weight: 800;
    font-size: 38px; line-height: 1.04; color: var(--white);
    text-shadow: 3px 4px 4px var(--title-shadow);
    letter-spacing: 0.5px;
  }
  .card--band .contact {
    position: absolute; left: 0; top: 242px; list-style: none;
    font-family: "Questrial", sans-serif; font-size: 17px; color: var(--ink); letter-spacing: 0.6px;
  }
  .card--band .contact li {
    display: block; width: max-content; background: var(--white);
    padding: 2px 14px 2px 44px; margin-bottom: 10px; line-height: 22px;
  }
  .card--band .contact li:nth-child(2) { padding-left: 34px; }
  .card--band .contact li:nth-child(3) { padding-left: 24px; }
</style>
</head>
<body>
<main class="sheet">

  <section class="card card--waves" aria-label="Business card, front">
    <svg class="decor" viewBox="0 0 760 434" aria-hidden="true">
      <path d="M420 0 C520 18 620 22 760 8 L760 18 C620 30 520 26 420 0 Z" fill="#ffffff"/>
      <path d="M470 0 C560 10 650 12 760 2 L760 0 Z" fill="#e6d5b8"/>
      <line x1="0" y1="186" x2="690" y2="176" stroke="#e6d5b8" stroke-width="3"/>
      <line x1="662" y1="178" x2="598" y2="366" stroke="#e6d5b8" stroke-width="2"/>
      <line x1="676" y1="178" x2="612" y2="366" stroke="#e6d5b8" stroke-width="2"/>
      <line x1="690" y1="176" x2="626" y2="366" stroke="#e6d5b8" stroke-width="2"/>
      <path d="M0 412 C180 395 360 430 560 398 C640 386 700 386 760 392 L760 402 C690 396 630 398 560 410 C360 442 180 408 0 424 Z" fill="#ffffff"/>
      <path d="M0 424 C200 410 380 440 560 414 C650 402 710 404 760 408 L760 434 L0 434 Z" fill="#b57a4b"/>
      <path d="M0 430 C200 418 380 446 560 422 C650 410 710 412 760 416 L760 434 L0 434 Z" fill="#e6d5b8"/>
    </svg>
    <h1 class="title">Still Harbour Counselling and Psychotherapy Wren Callow</h1>
    <ul class="contact">
      <li>Phone: 0412739506</li>
      <li>Email: wren.stillharbour@examplemail.test</li>
      <li>www.stillharbourcounselling&amp;psychotherapy.test</li>
    </ul>
  </section>

  <section class="card card--band" aria-label="Business card, alternate">
    <svg class="decor" viewBox="0 0 760 434" aria-hidden="true">
      <rect x="0" y="372" width="760" height="4" fill="#e6d5b8"/>
      <rect x="0" y="380" width="760" height="54" fill="#a88a66"/>
      <rect x="594" y="380" width="8" height="54" fill="#ffffff"/>
      <rect x="602" y="380" width="62" height="54" fill="#19787e"/>
      <rect x="664" y="380" width="8" height="54" fill="#ffffff"/>
    </svg>
    <h1 class="title">Still Harbour Counselling and Psychotherapy Wren Callow</h1>
    <ul class="contact">
      <li>Phone: 0412739506</li>
      <li>Email: wren.stillharbour@examplemail.test</li>
      <li>www.stillharbourcounselling&amp;psychotherapy.test</li>
    </ul>
  </section>

</main>
</body>
</html>
```